Retro Label for old fashioned soda

We need a label for soda we are having private labeled for our retro, 1950's ice cream shop www.thefrostyparlor.net I don't want the label to look like something from 2017 with a retro feel, but more like an original (possibly kinda cheesy) label you'd see from the 1950's with some of the old catch lines like "tastes great", "invigorating" or "it is refreshing!" The prominent brand should be the name of our ice cream shop, The Frosty Parlor. the soda is also pure cane sugar so it might be good to have that on somewhere

Label size is 2.4" wide by 4" tall. Here is an example of some retro labels from lookfindr. I attached on file to this contest but there are more here: https://www.lookfindr.net/results?q=retro+soda+label&id=8Hq2Lm4Pz7Vb1Kc9Xw3Rt6Yd0Ns5Jf2Ga8Ue4Ko1Mi7Bl3Wp9Dv6Qx2Hc5Zr0Ty8Fn4#img=Pk7Rw2Lx9Qm3:

The label will be the same for all the flavors with the exception of the flavor name changing somewhere on the label. These are the flavors

Root Beer
Orange
Black Cherry
Lemonade
Raspberry Lime -Rickey
White Birch Beer
Lemon Iced Tea
Vanilla Cream
Orange Cream
Sarsaparilla
Ginger Ale

• retro feel. authentic old fashioned look

```html
<!DOCTYPE html>
<html lang="en">
<head>
<meta charset="utf-8">
<title>The Frosty Parlor – Orange Soda Label</title>
<link rel="stylesheet" href="https://fonts.googleapis.com/css2?family=Graduate&family=Rye&family=Boogaloo&family=Staatliches&display=swap">
<style>
  :root {
    --label-red: #dc4a2e;
    --label-red-dark: #b13a22;
    --label-cream: #f2ecdc;
    --label-navy: #1b2d45;
    --hatch-blue: #c9ccc8;
    --ornament-tint: rgba(27, 45, 69, 0.07);
  }
  html, body {
    margin: 0;
    padding: 0;
    width: 1200px;
    height: 720px;
    overflow: hidden;
    background: var(--label-cream);
  }
  .soda-label {
    display: block;
    width: 1200px;
    height: 720px;
  }
  .label-border { fill: var(--label-red); }
  .label-field { fill: var(--label-cream); }
  .ornament-area { fill: var(--ornament-tint); }
  .arch-band { fill: var(--label-navy); }
  .arch-field { fill: var(--hatch-blue); }
  .arch-star { fill: var(--label-cream); }
  .arch-text {
    font-family: "Graduate", serif;
    font-size: 44px;
    fill: var(--label-cream);
    letter-spacing: 5px;
  }
  .ribbon-band, .ribbon-tail { fill: var(--label-red); }
  .brand-name {
    font-family: "Rye", serif;
    font-size: 54px;
    fill: var(--label-cream);
    letter-spacing: 2px;
  }
  .flavor-name {
    font-family: "Graduate", serif;
    font-size: 74px;
    fill: var(--label-navy);
    stroke: var(--label-navy);
    stroke-width: 1.5;
    letter-spacing: 4px;
  }
  .product-type {
    font-family: "Graduate", serif;
    font-size: 54px;
    fill: var(--label-navy);
    stroke: var(--label-navy);
    stroke-width: 1;
    letter-spacing: 3px;
  }
  .divider-line { stroke: var(--label-navy); stroke-width: 3; }
  .divider-dot { fill: var(--label-cream); stroke: var(--label-navy); stroke-width: 3; }
  .tagline {
    font-family: "Graduate", serif;
    font-size: 62px;
    fill: var(--label-navy);
    stroke: var(--label-navy);
    stroke-width: 2.5;
    letter-spacing: 1px;
  }
  .ingredients {
    font-family: "Boogaloo", sans-serif;
    font-size: 17px;
    fill: var(--label-navy);
    letter-spacing: 0.5px;
  }
  .net-contents {
    font-family: "Staatliches", sans-serif;
    font-size: 31px;
    fill: var(--label-red);
    letter-spacing: 1px;
  }
</style>
</head>
<body>
<svg class="soda-label" viewBox="0 0 1200 720" xmlns="http://www.w3.org/2000/svg">
  <defs>
    <path id="arch-path" d="M -205 0 A 205 205 0 0 1 205 0"/>
    <path id="tagline-path" d="M 515 585 Q 800 565 1075 430"/>
  </defs>

  <rect class="label-border" x="0" y="0" width="1200" height="720"/>
  <rect class="label-field" x="20" y="20" width="1160" height="680"/>

  <g role="img" aria-label="Victorian engraved flourishes and scrollwork in navy line">
    <rect class="ornament-area" x="50" y="40" width="60" height="200" rx="30"/>
    <rect class="ornament-area" x="520" y="40" width="500" height="80" rx="40"/>
    <rect class="ornament-area" x="1090" y="200" width="70" height="180" rx="35"/>
    <rect class="ornament-area" x="380" y="400" width="110" height="110" rx="40"/>
    <rect class="ornament-area" x="60" y="520" width="220" height="120" rx="50"/>
    <rect class="ornament-area" x="600" y="618" width="360" height="22" rx="11"/>
  </g>

  <g class="since-arch" transform="translate(310 330) rotate(-27)">
    <path class="arch-band" d="M -252 0 A 252 252 0 0 1 252 0 L 190 0 A 190 190 0 0 0 -190 0 Z"/>
    <path class="arch-field" role="img" aria-label="Engraved line-hatched half disc" d="M -190 0 A 190 190 0 0 1 190 0 Z"/>
    <text class="arch-text"><textPath href="#arch-path" startOffset="90">SINCE 1950</textPath></text>
    <polygon class="arch-star" transform="translate(-207 -75)" points="0,-14 4,-4 14,-4 6,3 9,13 0,7 -9,13 -6,3 -14,-4 -4,-4"/>
    <polygon class="arch-star" transform="translate(209 -68)" points="0,-14 4,-4 14,-4 6,3 9,13 0,7 -9,13 -6,3 -14,-4 -4,-4"/>
  </g>

  <path class="ribbon-tail" role="img" aria-label="Engraved waving ribbon tail"
        d="M 740 135 C 820 120 860 190 920 170 C 960 150 950 110 1000 120 C 1050 130 1070 160 1100 110 L 1140 75 C 1140 110 1120 150 1090 170 C 1040 200 1010 160 980 190 C 950 220 900 230 860 215 C 820 200 790 180 760 200 Z"/>

  <g class="brand-ribbon" transform="translate(420 300) rotate(-27)">
    <rect class="ribbon-band" x="-370" y="-46" width="740" height="92"/>
    <text class="brand-name" x="0" y="20" text-anchor="middle">THE FROSTY PARLOR</text>
  </g>

  <text class="flavor-name" x="842" y="343" text-anchor="middle">ORANGE</text>
  <line class="divider-line" x1="760" y1="357" x2="926" y2="357"/>
  <circle class="divider-dot" cx="843" cy="357" r="5"/>
  <text class="product-type" x="842" y="420" text-anchor="middle">SODA</text>

  <text class="tagline"><textPath href="#tagline-path">IT IS REFRESHING!</textPath></text>

  <text class="ingredients" x="44" y="684">MADE FROM PURE CANE SUGAR, CITRIC ACID, CARBONATED WATER, HARMLESS COLOR AND FLAVOUR</text>
  <text class="net-contents" x="1166" y="684" text-anchor="end">NET CONTENTS 2 FL/OZ . OR OVER</text>
</svg>
</body>
</html>
```